Cleaning and Maintenance Business card design

i provide a service which includes;
Professional Window Cleaning
Lawn Mowing
Gardening
Painting
Rubbish Removal
Commercial Cleaning
Property & Ground Maintenance
Pensioner discounts apply
Call now for an inquiry and free quote
`Double sided` (willing to pay any extra)
i would like a design that is not too crowded and straight to the point.
i want the reader to know exactly what the business is about from one glance.
i would like the logo to communicate the businesses 3 main aspects (window cleaning, lawn mowing, and Cleaning)
Thanks.
Contact Information for Business Card
Business name : Brick 4 Leaf*
* with subline 'And Everything In Between' (smaller font)
Name: Tom Varkonisky
Mobile: 0417 582 903
Email: t.varkonisky@mailbrook.net
ABN: 47 915 230 861
`Double Sided`
Logo Text
Brick 4 Leaf

```html
<!DOCTYPE html>
<html lang="en">
<head>
<meta charset="utf-8">
<title>Brick 4 Leaf – Business Card</title>
<link href="https://fonts.googleapis.com/css2?family=Kalam:wght@400;700&display=swap" rel="stylesheet">
<style>
  :root {
    --paper: #ffffff;
    --grass-light: #6fd43a;
    --grass-mid: #4fbf1f;
    --grass-deep: #3a9e12;
    --ink: #ffffff;
    --tool-red: #d9302a;
    --tool-grey: #b9b9b9;
  }
  html, body {
    margin: 0;
    padding: 0;
    width: 1200px;
    height: 695px;
    overflow: hidden;
    background: var(--paper);
  }
  .card {
    position: relative;
    width: 1200px;
    height: 695px;
    background: var(--paper);
    font-family: "Kalam", cursive;
    color: var(--ink);
  }
  .lawn {
    position: absolute;
    left: 18px;
    top: 22px;
    width: 1164px;
    height: 646px;
    background:
      repeating-linear-gradient(90deg, rgba(255,255,255,0.05) 0 90px, rgba(0,0,0,0.04) 90px 180px),
      radial-gradient(ellipse at 55% 45%, var(--grass-light) 0%, var(--grass-mid) 55%, var(--grass-deep) 100%);
  }
  .tools-art {
    position: absolute;
    left: 24px;
    top: 28px;
    width: 334px;
    height: 210px;
    background: radial-gradient(ellipse at 45% 55%, var(--tool-red) 0%, #c9403a 40%, var(--tool-grey) 75%, rgba(255,255,255,0.55) 100%);
    border-radius: 6px;
  }
  .brand {
    position: absolute;
    left: 300px;
    right: 24px;
    top: 72px;
    margin: 0;
    font-size: 132px;
    font-weight: 400;
    line-height: 1;
    text-align: center;
    white-space: nowrap;
  }
  .tagline {
    position: absolute;
    left: 20px;
    top: 238px;
    margin: 0;
    font-size: 46px;
    font-weight: 400;
    line-height: 1;
  }
  .services {
    position: absolute;
    left: 25px;
    top: 318px;
    margin: 0;
    padding: 0;
    list-style: none;
    font-size: 37px;
    line-height: 50px;
    letter-spacing: 1px;
  }
  .contact {
    position: absolute;
    right: 26px;
    top: 348px;
    text-align: right;
  }
  .contact .name {
    margin: 0 24px 10px 0;
    font-size: 46px;
    font-weight: 700;
    line-height: 1.1;
  }
  .contact p {
    margin: 0;
    font-size: 33px;
    line-height: 57px;
    letter-spacing: 0.5px;
  }
  .contact .mobile { margin-right: 18px; }
  .discount {
    position: absolute;
    right: 28px;
    bottom: 36px;
    margin: 0;
    font-size: 26px;
    font-weight: 700;
  }
</style>
</head>
<body>
  <div class="card">
    <div class="lawn" role="img" aria-label="Close-up photograph of a freshly mown striped green lawn"></div>
    <div class="tools-art" role="img" aria-label="Illustration of a red lawn mower with a window squeegee and a broom"></div>

    <h1 class="brand">Brick 4 Leaf</h1>
    <p class="tagline">and everything in between</p>

    <ul class="services">
      <li>Window Cleaning</li>
      <li>Lawn Mowing</li>
      <li>Gardening</li>
      <li>Painting</li>
      <li>Waste Removal</li>
      <li>Commercial Cleaning</li>
      <li>Property &amp; Ground Maintenance</li>
    </ul>

    <div class="contact">
      <h2 class="name">Tom Varkonisky</h2>
      <p class="mobile">mob: 0417 582 903</p>
      <p class="email">email: t.varkonisky@mailbrook.net</p>
      <p class="abn">ABN: 47 915 230 861</p>
    </div>

    <p class="discount">Pensioners Discounts Apply</p>
  </div>
</body>
</html>
```